Dental care for hole family, announcement in newspaper

Hey! I have Dental surgery Business in middle of Finland in Jyväskylä. You can see my web www.hammasvelmora.fi.
Now I am looking for new way to do advertisement, more visual I hope.
I woul like to have announcement in newspaper. I would like to tell that we treating hole family from babyes to seniors. I saw here in your pages cute photo where about 1-year old baby was brushing teeth ja looking with big eys to me. It is the feeling I am looking for. My idea is to tell people, that in our klinik, they can have "own dental hygienist" who is taking care of them with dentists of different spesialitis.
Now I need advertisements for that information!!

Yours, Velmora

Target Market(s)

All.

Industry/Entity Type

Dental Clinic

Requirements
Must have
• Visual components, whicts are matching with my homepages visual look (www.hammasvelmora.fi).
Nice to have
• My logo, whitch you can find from my webpages.

```html
<!DOCTYPE html>
<html lang="en">
<head>
<meta charset="utf-8">
<title>Hammasvelmora – Family Dental Poster</title>
<link href="https://fonts.googleapis.com/css2?family=Montserrat:ital,wght@0,400;0,600;0,700;0,800;1,800&display=swap" rel="stylesheet">
<style>
  :root{
    --brown:#7a4a1e;
    --brown-dark:#5e3713;
    --blue:#1b8fcf;
    --blue-deep:#135f98;
    --sky:#6cc6ef;
    --orange:#f7a81b;
    --white:#ffffff;
    --ink:#3a3a3a;
    --page:#f2f0ec;
  }
  *{box-sizing:border-box;margin:0;padding:0}
  html,body{width:1200px;height:1200px;overflow:hidden;background:var(--page);font-family:"Montserrat",Arial,sans-serif}
  .poster{position:absolute;left:180px;top:20px;width:840px;height:1160px;background:var(--white);overflow:hidden;box-shadow:0 4px 18px rgba(0,0,0,.12)}
  .poster-art{position:absolute;inset:0}
  .tooth-mark{position:absolute;left:44px;top:34px;width:96px;height:96px;border-radius:22px;background:var(--sky)}
  .clinic-name{position:absolute;right:40px;top:40px;text-align:right;color:var(--brown);font-weight:600}
  .clinic-name .sub{font-size:15px;letter-spacing:1px}
  .clinic-name .main{font-size:30px;letter-spacing:2px;line-height:1.1}
  .clinic-name .partner{font-size:12px;color:var(--brown)}
  .headline{position:absolute;left:44px;top:150px;font-size:50px;font-weight:800;color:var(--orange);white-space:nowrap}
  .headline span{color:var(--sky)}
  .tagline{position:absolute;left:44px;right:40px;top:218px;border-top:2px solid var(--ink);border-bottom:2px solid var(--ink);padding:6px 0;font-size:22px;letter-spacing:1px;color:var(--ink);text-transform:uppercase}
  .tagline b{font-weight:800}
  .intro{position:absolute;left:50px;top:700px;width:560px;color:var(--white)}
  .intro h2{font-size:20px;font-weight:600;text-transform:uppercase;margin-bottom:6px}
  .intro p{font-size:18px;line-height:1.35}
  .services-title{position:absolute;left:50px;top:838px;font-size:30px;color:var(--white)}
  .services{position:absolute;left:50px;right:30px;top:915px;display:flex;gap:34px;list-style:none;color:var(--white);font-size:22px}
  .services li{display:flex;align-items:center;gap:10px}
  .services svg{width:34px;height:34px}
  .offer{position:absolute;left:590px;top:715px;width:200px;height:200px;display:flex;flex-direction:column;align-items:center;justify-content:center;color:var(--white);text-align:center}
  .offer .big{font-size:48px;font-weight:800;line-height:1}
  .offer .small{font-size:15px;font-weight:700;letter-spacing:1px}
  .website{position:absolute;left:44px;top:1040px;font-size:46px;font-weight:800;font-style:italic;color:var(--orange)}
  .call{position:absolute;right:40px;top:1030px;color:var(--white);text-align:left}
  .call .label{display:flex;align-items:center;gap:8px;font-size:16px;font-weight:700}
  .call .label svg{width:28px;height:28px}
  .call .number{margin-top:4px;border:2px solid var(--white);padding:4px 14px;font-size:34px;font-weight:800;letter-spacing:2px}
</style>
</head>
<body>
<main class="poster">
  <svg class="poster-art" viewBox="0 0 840 1160" width="840" height="1160">
    <defs>
      <linearGradient id="photoSenior" x1="0" y1="0" x2="1" y2="1">
        <stop offset="0" stop-color="#eef2f5"/><stop offset="1" stop-color="#d9b8a3"/>
      </linearGradient>
      <linearGradient id="photoChild" x1="0" y1="0" x2="1" y2="1">
        <stop offset="0" stop-color="#c9dbe6"/><stop offset="1" stop-color="#e8cfa0"/>
      </linearGradient>
      <linearGradient id="blueBand" x1="0" y1="0" x2="0" y2="1">
        <stop offset="0" stop-color="var(--blue)"/><stop offset="1" stop-color="var(--blue-deep)"/>
      </linearGradient>
    </defs>
    <rect x="0" y="275" width="430" height="360" fill="url(#photoSenior)" role="img" aria-label="Photo of a smiling senior man brushing his teeth"/>
    <rect x="430" y="290" width="410" height="345" fill="url(#photoChild)" role="img" aria-label="Photo of a young girl brushing her teeth"/>
    <path d="M0 560 C250 650 600 670 840 650 L840 1160 L0 1160 Z" fill="var(--brown)"/>
    <path d="M0 615 C260 700 600 720 840 700 L840 1000 L0 1000 Z" fill="url(#blueBand)"/>
    <g fill="var(--orange)" transform="translate(690 815)">
      <rect x="-78" y="-78" width="156" height="156"/>
      <rect x="-78" y="-78" width="156" height="156" transform="rotate(15)"/>
      <rect x="-78" y="-78" width="156" height="156" transform="rotate(30)"/>
      <rect x="-78" y="-78" width="156" height="156" transform="rotate(45)"/>
      <rect x="-78" y="-78" width="156" height="156" transform="rotate(60)"/>
      <rect x="-78" y="-78" width="156" height="156" transform="rotate(75)"/>
    </g>
  </svg>

  <div class="tooth-mark" role="img" aria-label="Tooth illustration"></div>

  <div class="clinic-name">
    <div class="sub">Hammaslääkäriasema</div>
    <div class="main">HAMMASVELMORA</div>
    <div class="partner">kuntovire</div>
  </div>

  <h1 class="headline">Dental Care <span>You Can Own</span></h1>
  <div class="tagline">A <b>Specialist</b> Dentist for the Whole Family</div>

  <section class="intro">
    <h2>We are the trusted family dentist since 1983</h2>
    <p>and since then we have been keeping many of our client's teeth problem free and clean throughout the years.</p>
  </section>

  <h3 class="services-title">Our Services :</h3>
  <ul class="services">
    <li><svg viewBox="0 0 34 34"><rect x="2" y="6" width="26" height="26" fill="none" stroke="#fff" stroke-width="3"/><path d="M8 18 L15 25 L32 4" fill="none" stroke="#fff" stroke-width="4"/></svg>Floss &amp; Cleaning</li>
    <li><svg viewBox="0 0 34 34"><rect x="2" y="6" width="26" height="26" fill="none" stroke="#fff" stroke-width="3"/><path d="M8 18 L15 25 L32 4" fill="none" stroke="#fff" stroke-width="4"/></svg>Teeth Checking</li>
    <li><svg viewBox="0 0 34 34"><rect x="2" y="6" width="26" height="26" fill="none" stroke="#fff" stroke-width="3"/><path d="M8 18 L15 25 L32 4" fill="none" stroke="#fff" stroke-width="4"/></svg>Repair &amp; Fix</li>
  </ul>

  <div class="offer"><span class="big">FREE</span><span class="small">CONSULTATION</span></div>

  <div class="website">Hammasvelmora.fi</div>

  <div class="call">
    <div class="label"><svg viewBox="0 0 24 24"><path d="M6.6 10.8a15 15 0 0 0 6.6 6.6l2.2-2.2a1 1 0 0 1 1-.25 11.4 11.4 0 0 0 3.6.57 1 1 0 0 1 1 1V20a1 1 0 0 1-1 1A17 17 0 0 1 3 4a1 1 0 0 1 1-1h3.5a1 1 0 0 1 1 1c0 1.25.2 2.45.57 3.57a1 1 0 0 1-.25 1z" fill="#fff"/></svg>CALL US</div>
    <div class="number">014 555 0192</div>
  </div>
</main>
</body>
</html>
```